Design the World's Greatest Valentine's Day Greeting Card

We're looking for designers who can create the best Valentine's Day greeting card designs in the world. Your design could be could be extra special because it is funny, beautiful, inspiring or original.

Your designs should be able to fit on a standard 4"x6" greeting card. The main design will need to be for the front page (cover) of the card, but you can also include some design for the inside pages if you like.

Multiple winners will be awarded, and will be chosen within 5 days after the contest ends on February 13, 2019.
First Prize: $200
Runners-up: $100 each

The winning card design (or designs) could be recognised as standout designs publicly, as they can be used, by Gigmarten.com, at it sole discretion, in some Gigmarten.com marketing or PR materials.

Let's celebrate Valentine's Day together by showcasing your designs!

```html
<!DOCTYPE html>
<html lang="en">
<head>
<meta charset="utf-8">
<title>Happy Valentine's Day Card</title>
<link rel="stylesheet" href="https://fonts.googleapis.com/css2?family=Josefin+Sans:wght@400;600&display=swap">
<style>
  :root {
    --backdrop: #f1f1f1;
    --coral: #ee5a6f;
    --blush: #f7c3c9;
    --quote-ink: #e4465f;
    --cover-ink: #ffffff;
    --art-violet: #7a4a9c;
    --art-lime: #b9d27a;
    --art-gold: #e9b63e;
  }
  html, body {
    margin: 0;
    padding: 0;
    width: 1200px;
    height: 777px;
    overflow: hidden;
    background: var(--backdrop);
  }
  .canvas {
    position: relative;
    width: 1200px;
    height: 777px;
    font-family: "Josefin Sans", sans-serif;
  }
  .card-inside {
    position: absolute;
    left: 80px;
    top: 148px;
    width: 640px;
    height: 480px;
    background: var(--coral);
    box-shadow: 0 2px 10px rgba(0,0,0,0.08);
  }
  .card-inside .big-heart {
    position: absolute;
    inset: 0;
  }
  .quote {
    position: absolute;
    left: 150px;
    top: 172px;
    width: 340px;
    margin: 0;
    text-align: center;
    color: var(--quote-ink);
    font-size: 13px;
    font-weight: 400;
    letter-spacing: 0.2em;
    line-height: 1.9;
    text-transform: uppercase;
  }
  .quote cite {
    display: block;
    font-style: normal;
  }
  .card-cover {
    position: absolute;
    left: 800px;
    top: 148px;
    width: 320px;
    height: 480px;
    background: var(--coral);
    box-shadow: 0 2px 10px rgba(0,0,0,0.08);
  }
  .cover-art {
    position: absolute;
    left: 28px;
    top: 62px;
    width: 264px;
    height: 314px;
    background: linear-gradient(160deg, var(--art-violet) 0%, var(--art-lime) 45%, var(--art-gold) 100%);
  }
  .cover-greeting {
    position: absolute;
    left: 0;
    right: 0;
    bottom: 58px;
    margin: 0;
    text-align: center;
    color: var(--cover-ink);
    font-size: 17px;
    font-weight: 600;
    letter-spacing: 0.2em;
  }
</style>
</head>
<body>
<main class="canvas">
  <section class="card-inside">
    <svg class="big-heart" viewBox="0 0 640 480" width="640" height="480" aria-hidden="true">
      <path d="M320 470 L62 222 L118 40 L252 30 L320 132 L398 38 L566 50 L602 214 Z" fill="var(--blush)"/>
    </svg>
    <blockquote class="quote">
      &ldquo;There is only one happiness in life &ndash;<br>
      to love and be loved&rdquo;
      <cite>Mara Lindqvist</cite>
    </blockquote>
  </section>

  <section class="card-cover">
    <div class="cover-art" role="img" aria-label="Colourful illustrated portrait of a woman with curly hair in a yellow top"></div>
    <h1 class="cover-greeting">HAPPY VALENTINE&rsquo;S DAY</h1>
  </section>
</main>
</body>
</html>
```